Restaurant Menu Design for Meal Prep offered in a food display cooler at a local Gym

I am looking for a menu design with the following items . I would like a workable copy if possible so in the future we can change pricing on this file , or change items . This file will be uploaded on a USB drive and then plugged into a TV. Please ensure a JPEG file is included so this will also work on this TV.

Have a look at our website , www.quilvarkitchen.com for ideas for design that represent the brand appropriately.
The below are the menu items that we would need displayed along with their pricing.

BREAKFAST MEAL PREP ITEMS
Blueberry Pancakes $12.00
Copper Lantern Burrito $10.95

LUNCH/DINNER MEAL PREP OPTIONS
BBQ Glazed Salmon $16.50
Cheeseburger Bowl $13.50
Chicken Alfredo $12.00
Pesto Chicken Pasta $12.00
Chicken Parmesan $13.00
Taco Bowl $14.00
Steak Bite and Green Stir Fry $12.00
Asian Chicken Teriyaki $12.00
Marlowe Stir Fry $15.95

I will attach our logo below, this will need to be on the design. The "heading" (for example breakfast meal prep items and lunch/dinner meal prep options) for the menu should also be on the design.

Ive attached a couple of photos that you need to add to your design.

This will be displayed in a GYM

Meal Prep + Fitness Industry

• Quilvar Logo and Photos attached
• Maybe incorporate something that represents working out or healthy lifestyle in design without going too overboard

```html
<!DOCTYPE html>
<html lang="en">
<head>
<meta charset="utf-8">
<title>Quilvar Meal Prep Menu</title>
<link href="https://fonts.googleapis.com/css2?family=League+Spartan:wght@500;600;700;800&display=swap" rel="stylesheet">
<style>
  :root {
    --ink: #111111;
    --heading-ink: #1e2a0f;
    --lime: #8dc63f;
    --logo-grey: #cfcfcf;
    --panel-white: rgba(255, 255, 255, 0.82);
    --wood-light: #f1f3f4;
    --wood-mid: #dfe4e7;
    --wood-blue: #c9d6dd;
  }
  * { margin: 0; padding: 0; box-sizing: border-box; }
  html, body { width: 1200px; height: 800px; overflow: hidden; }
  body { font-family: "League Spartan", "Helvetica Neue", Arial, sans-serif; color: var(--ink); }

  .menu-board {
    position: relative;
    width: 1200px;
    height: 800px;
    overflow: hidden;
    background: linear-gradient(100deg, var(--wood-light) 0%, var(--wood-mid) 30%, var(--wood-light) 55%, var(--wood-blue) 80%, var(--wood-light) 100%);
  }

  .brand-block {
    position: absolute;
    left: 0; top: 0;
    width: 562px; height: 147px;
    background: var(--ink);
    padding: 28px 0 0 86px;
  }
  .brand-name {
    display: block;
    font-size: 70px;
    font-weight: 700;
    line-height: 1;
    letter-spacing: 1px;
    color: var(--logo-grey);
  }
  .brand-tagline {
    display: block;
    margin-top: 8px;
    font-size: 21px;
    font-weight: 700;
    color: var(--lime);
    letter-spacing: 0.3px;
    word-spacing: 2px;
  }

  .section-band {
    position: absolute;
    height: 75px;
    background: var(--lime);
    display: flex;
    align-items: center;
    font-size: 29px;
    font-weight: 600;
    color: var(--heading-ink);
    letter-spacing: 0.2px;
  }
  .section-band--breakfast { left: 0; top: 205px; width: 525px; padding-left: 22px; }
  .section-band--lunch { left: 563px; top: 303px; width: 637px; padding-left: 26px; }

  .item-panel--breakfast {
    position: absolute;
    left: 0; top: 280px;
    width: 525px; height: 125px;
    background: var(--panel-white);
    padding: 22px 38px 0 16px;
  }
  .item-list { list-style: none; }
  .menu-item {
    display: flex;
    justify-content: space-between;
    font-size: 28px;
    font-weight: 600;
    line-height: 1;
  }
  .item-panel--breakfast .menu-item { height: 41px; padding-top: 4px; }

  .item-panel--lunch {
    position: absolute;
    left: 578px; top: 404px;
    width: 610px;
  }
  .item-panel--lunch .menu-item { height: 44.5px; }

  .food-photo { position: absolute; }
  .food-photo--pancakes {
    left: 563px; top: 0; width: 637px; height: 303px;
    background: radial-gradient(ellipse at 55% 55%, #f3e2c4 0%, #e2b77c 28%, #ffffff 52%, #eceff1 100%);
  }
  .food-photo--pasta {
    left: 0; top: 440px; width: 525px; height: 320px;
    background: radial-gradient(ellipse at 50% 42%, #c9a98a 0%, #8e9a55 35%, #ffffff 62%, rgba(255,255,255,0) 80%);
  }
</style>
</head>
<body>
<main class="menu-board">
  <header class="brand-block">
    <span class="brand-name">QUILVAR</span>
    <span class="brand-tagline">HEALTHY KITCHEN | MEAL PREP</span>
  </header>

  <div class="food-photo food-photo--pancakes" role="img" aria-label="Stack of blueberry pancakes with yogurt drizzle and fresh blueberries on a white plate"></div>

  <h2 class="section-band section-band--breakfast">BREAKFAST MEAL PREP ITEMS</h2>
  <section class="item-panel--breakfast">
    <ul class="item-list">
      <li class="menu-item"><span>Blueberry Pancakes</span><span>$12.00</span></li>
      <li class="menu-item"><span>Copper Lantern Burrito</span><span>$10.95</span></li>
    </ul>
  </section>

  <div class="food-photo food-photo--pasta" role="img" aria-label="White bowl of pesto chicken penne with broccoli, peppers and grated parmesan"></div>

  <h2 class="section-band section-band--lunch">LUNCH/DINNER MEAL PREP OPTIONS</h2>
  <section class="item-panel--lunch">
    <ul class="item-list">
      <li class="menu-item"><span>BBQ Glazed Salmon</span><span>$16.50</span></li>
      <li class="menu-item"><span>Cheeseburger Bowl</span><span>$13.50</span></li>
      <li class="menu-item"><span>Chicken Alfredo</span><span>$12.00</span></li>
      <li class="menu-item"><span>Pesto Chicken Pasta</span><span>$12.00</span></li>
      <li class="menu-item"><span>Chicken Parmesan</span><span>$13.00</span></li>
      <li class="menu-item"><span>Taco Bowl</span><span>$14.00</span></li>
      <li class="menu-item"><span>Steak Bite and Green Stir Fry</span><span>$12.00</span></li>
      <li class="menu-item"><span>Asian Chicken Teriyaki</span><span>$12.00</span></li>
      <li class="menu-item"><span>Marlowe Stir Fry</span><span>$15.95</span></li>
    </ul>
  </section>
</main>
</body>
</html>
```